Pflegedienst sucht Flyerdesign
Zielgruppe
Wir sind ein ambulanter Pflegedienst und betreuen ca. 200 Patienten in ländlicher Region. Unsere Zielgruppe sind Pflegebedürftige aus altersbedingten Gründen oder nach Krankenhausaufenthalten. Wir setzen auf Qualität, Zuverlässigkeit, Exklusivität.
Aufgabenstellung
DIN lang Flyer. Wir werben ganz bewußt nicht mit Bildern von Senioren oder alten Menschen, weil das fast alle Pflegedienste tun. Daher setzen wir eher auf Motive aus unserer Urlaubsregion: Strand, Meer...
Unseren Firmen-Vebo hätten wir gern als Fotoausschnitt ohne Hintergund mit dabei.
Und einen Kartenausschnitt mit unserem Einzugsgebiet fänden wir toll. Dies umfasst ca. 15 km um Laboe und Heikendorf folgende Orte: Stein, Wendtorf, Probsteierhagen, Schönkirchen und Mönkeberg.

```html
<!DOCTYPE html>
<html lang="de">
<head>
<meta charset="utf-8">
<title>Pflegedienst Flyer Innenseite</title>
<link rel="stylesheet" href="https://fonts.googleapis.com/css2?family=Merriweather:wght@300;400;700&display=swap">
<style>
  :root {
    --sky-top: #3f86c6;
    --sky-mid: #68a9d8;
    --sky-low: #a9cfe6;
    --sea: #3a7bb0;
    --sea-deep: #2f6a9c;
    --sand: #e9e7e3;
    --sand-dark: #d9d6d0;
    --white: #ffffff;
    --panel: rgba(255, 255, 255, 0.86);
    --accent: #a8235a;
  }
  * { margin: 0; padding: 0; box-sizing: border-box; }
  html, body { width: 1200px; height: 848px; overflow: hidden; }
  body { font-family: "Merriweather", Georgia, serif; color: var(--white); }

  .spread { position: relative; width: 1200px; height: 848px; overflow: hidden; }

  .beach-scene {
    position: absolute; inset: 0;
    background: linear-gradient(180deg,
      var(--sky-top) 0%, var(--sky-mid) 35%, var(--sky-low) 63%,
      var(--sea) 64.5%, var(--sea-deep) 70%, #6a9fc2 74.5%,
      var(--sand) 75.5%, var(--sand-dark) 100%);
  }

  .column { position: absolute; top: 44px; }
  .column--left { left: 41px; width: 340px; }
  .column--middle { left: 432px; width: 350px; }
  .column--right { left: 823px; width: 350px; }

  .column__title {
    font-weight: 300; font-size: 21.5px; line-height: 29px;
    letter-spacing: 0.3px; margin-bottom: 22px;
  }
  .column--middle .column__title { margin-bottom: 14px; }
  .column--right .column__title { margin-bottom: 31px; }

  .section-title { font-weight: 700; font-size: 15px; line-height: 20px; margin-bottom: 6px; }
  .section-title + .plus-list { margin-top: 0; }
  .plus-list + .section-title { margin-top: 20px; }

  .plus-list { list-style: none; font-weight: 400; font-size: 12.6px; line-height: 20px; }
  .plus-list li { position: relative; padding-left: 12px; margin-bottom: 5.5px; }
  .plus-list li::before { content: "+"; position: absolute; left: 0; }
  .plus-list--tight li.joined { margin-bottom: 0; }

  .map-panel {
    position: absolute; left: 40px; top: 415px; width: 331px; height: 356px;
    background: var(--panel);
    display: flex; align-items: center; justify-content: center;
  }
  .map-panel__label { color: var(--accent); font-weight: 700; font-size: 18px; margin-top: -3px; }

  .strengths {
    position: absolute; left: 821px; top: 404px; width: 335px; height: 275px;
    background: var(--panel); padding: 32px 20px 0 26px; color: var(--accent);
  }
  .strengths__title { font-weight: 700; font-size: 16px; letter-spacing: 0.4px; margin-bottom: 6px; }
  .strengths__list { list-style: none; font-size: 12.6px; line-height: 20px; }
  .strengths__list li { position: relative; padding-left: 12px; margin-bottom: 5px; }
  .strengths__list li::before { content: "•"; position: absolute; left: 0; }
</style>
</head>
<body>
<main class="spread">
  <div class="beach-scene" role="img" aria-label="Foto: Sandstrand an der Ostsee mit blauem Meer und wolkenlosem Himmel"></div>

  <section class="column column--left">
    <h2 class="column__title">Als Vertragspartner aller Kranken- und Pflegekassen helfen wir, wo wir können:</h2>
    <ul class="plus-list">
      <li>bei Pflegebedürftigkeit</li>
      <li>bei Krankheit oder nach Entbindungen</li>
      <li>bei Behinderung und Einschränkungen im Alltag besonders bei Demenz</li>
      <li>nach Krankenhausaufenthalten oder ambulanten Operationen</li>
      <li>bei Verhinderung der privaten Pflegepersonen in der letzten Lebensphase zu Hause</li>
      <li>bei Urlaub mit Pflegebedürftigkeit in unserer Region</li>
    </ul>
  </section>

  <div class="map-panel">
    <span class="map-panel__label">Umgebungskarte</span>
  </div>

  <section class="column column--middle">
    <h2 class="column__title">Und kümmern uns je nach Bedarf mehrmals täglich um Sie:</h2>
    <h3 class="section-title">Im Rahmen ärztlicher Verordnungen</h3>
    <ul class="plus-list">
      <li>versorgen wir Wunden und wechseln Verbände</li>
      <li>verabreichen wir Injektionen</li>
      <li>stellen wir Medikamente und überwachen die Einnahme</li>
      <li>ziehen wir Kompressionsstrümpfe an und aus</li>
      <li>messen wir Blutdruck und Blutzucker</li>
    </ul>
    <h3 class="section-title">Im Rahmen der Pflegekasse</h3>
    <ul class="plus-list plus-list--tight">
      <li>helfen wir bei der täglichen Körperpflege oder leiten Sie an</li>
      <li>beobachten wir umfassend Ihren Allgemeinzustand</li>
      <li>machen Bewegungsübungen, Spaziergänge oder begleiten Sie zum Arzt oder Aktivitäten</li>
      <li class="joined">bereiten wir Ihnen Essen zu und kaufen ein</li>
      <li>unterstützen wir bei der hauswirtschaftliche Versorgung</li>
    </ul>
  </section>

  <section class="column column--right">
    <h2 class="column__title">Unser motiviertes und freundliches Team besteht aus:</h2>
    <ul class="plus-list">
      <li>Examinierten Pflegefach- &amp; Führungskräften</li>
      <li>Palliativfachkräften</li>
      <li>Wundmanagern</li>
      <li>Hygienefachkräften</li>
      <li>Pflegeberatern</li>
      <li>Haus- &amp; Familienpfleger/innen</li>
      <li>Betreuungskräften &amp; Beschäftigungsassistenten</li>
      <li>Hauswirtschaftler/innen</li>
      <li>Kaufmännischen Verwaltungskräften</li>
    </ul>
  </section>

  <aside class="strengths">
    <h3 class="strengths__title">Unsere Stärken:</h3>
    <ul class="strengths__list">
      <li>sehr gute, PQK-geprüfte Pflegequalität</li>
      <li>Ehrlichkeit, Transparenz, Fairness</li>
      <li>individuelle Rundumversorgung und partnerschaftlicher Umgang</li>
      <li>inhabergeführtes Unternehmen mit schlanken Strukturen und über 20 Jahren Erfahrung</li>
      <li>angenehmes, familiäres Arbeitsklima</li>
    </ul>
  </aside>
</main>
</body>
</html>
```